Kovalen Spinal Care and Performance

We need new business cards, something more modern, clean. On the back of the card maybe a quote. The Dr. likes, “The doctor of the future will give no medicine, but will interest his patient in the care of the human frame, in diet and in the cause and prevention of disease.” - Walter Brisby. We are open to other suggestions. We are a chiropractic office.

```html
<!DOCTYPE html>
<html lang="en">
<head>
<meta charset="utf-8">
<title>Kovalen Spinal Care and Performance – Business Card</title>
<link href="https://fonts.googleapis.com/css2?family=Cinzel:wght@400;600&family=Arimo:wght@400&family=Great+Vibes&display=swap" rel="stylesheet">
<style>
  :root {
    --backdrop: #d8d2c9;
    --card: #ffffff;
    --purple: #6a2f7c;
    --purple-dark: #55305f;
    --ink: #4a4a4a;
    --quote-ink: #555555;
  }
  * { margin: 0; padding: 0; box-sizing: border-box; }
  html, body { width: 1189px; height: 1200px; overflow: hidden; }
  body {
    background: var(--backdrop);
    position: relative;
    font-family: "Arimo", Arial, sans-serif;
  }
  .card {
    position: absolute;
    left: 169px;
    width: 851px;
    height: 485px;
    background: var(--card);
    border-radius: 23px;
    overflow: hidden;
    box-shadow: 0 6px 18px rgba(0,0,0,0.25);
  }
  .card--front { top: 112px; }
  .card--back { top: 641px; }

  .side-panel {
    position: absolute;
    top: 0; right: 0;
    width: 215px; height: 100%;
    background: linear-gradient(90deg, var(--purple-dark), var(--purple));
  }

  .brand { position: absolute; left: 43px; top: 78px; color: var(--purple); font-family: "Cinzel", serif; font-weight: 400; }
  .brand__name { font-size: 68px; line-height: 1; letter-spacing: 1px; }
  .brand__tagline { font-size: 17px; margin-top: 6px; margin-left: 4px; letter-spacing: 0.5px; }

  .contact { position: absolute; left: 43px; top: 262px; color: var(--ink); }
  .contact__name { font-family: "Cinzel", serif; font-weight: 600; font-size: 22px; color: var(--purple); letter-spacing: 0.5px; }
  .contact__role { font-size: 18px; margin-top: -2px; }
  .contact__address { font-size: 19px; line-height: 25px; margin-top: 18px; }
  .contact__lines { list-style: none; margin-top: 12px; font-size: 19px; line-height: 26px; }
  .contact__lines li { display: flex; align-items: center; gap: 7px; }
  .contact__icon { width: 20px; height: 20px; flex: none; }

  .quote {
    position: absolute; left: 0; right: 0; top: 193px;
    text-align: center; color: var(--quote-ink);
    font-size: 19px; line-height: 25px;
  }
  .quote__author { font-family: "Great Vibes", cursive; font-size: 24px; margin-top: 2px; color: #666; }
</style>
</head>
<body>
  <section class="card card--front" aria-label="Business card front">
    <div class="side-panel" role="img" aria-label="Decorative purple side band with green curved accent"></div>

    <div class="brand">
      <div class="brand__name">KOVALEN</div>
      <div class="brand__tagline">SPINAL CARE &amp; PERFORMANCE</div>
    </div>

    <div class="contact">
      <div class="contact__name">Dr. Walter Brisby</div>
      <div class="contact__role">Owner</div>
      <div class="contact__address">412 W Larchmont Ave, Suite C<br>Ridgefield, Illinois 60418</div>
      <ul class="contact__lines">
        <li>
          <svg class="contact__icon" viewBox="0 0 20 20" aria-hidden="true">
            <circle cx="10" cy="10" r="10" fill="var(--purple)"/>
            <path d="M7 5 L9 5 L10 8 L8.6 9 C9.2 10.6 10 11.5 11.2 12 L12 10.6 L15 11.6 L15 13.5 C15 14.4 14 15 13 14.8 C9 14 6 11 5.3 7 C5.1 6 5.8 5 7 5 Z" fill="#fff"/>
          </svg>
          (555) 304-2187
        </li>
        <li>
          <svg class="contact__icon" viewBox="0 0 20 20" aria-hidden="true">
            <circle cx="10" cy="10" r="10" fill="var(--purple)"/>
            <g fill="none" stroke="#fff" stroke-width="1">
              <circle cx="10" cy="10" r="5.5"/>
              <ellipse cx="10" cy="10" rx="2.5" ry="5.5"/>
              <line x1="4.5" y1="10" x2="15.5" y2="10"/>
            </g>
          </svg>
          www.kovalenspinalcare.com
        </li>
      </ul>
    </div>
  </section>

  <section class="card card--back" aria-label="Business card back">
    <blockquote class="quote">
      <p>“The doctor of the future will give no medicine,<br>
      but will interest his patient in the care<br>
      of the human frame, in diet and in the cause and prevention of disease.”</p>
      <p class="quote__author">- Walter Brisby -</p>
    </blockquote>
  </section>
</body>
</html>
```